Business Card Design

Hoping for a black background business card, minimalistic design.
With the Marble Crest logo you created in white.

I would like to include:
My Name and title
Address (street address)
Reception: (phone number)
Fax: (fax number)
Reception: (email address)
Direct email: (email address)
Instagram: (ig handle)

```html
<!DOCTYPE html>
<html lang="en">
<head>
<meta charset="utf-8">
<title>Marble Crest Business Card</title>
<link href="https://fonts.googleapis.com/css2?family=Montserrat:wght@400;500;600;700&display=swap" rel="stylesheet">
<style>
  :root {
    --page-bg: #3a3a3a;
    --card-bg: #1d1d1e;
    --card-edge: #2a2a2b;
    --text-light: #f2f2f2;
    --text-soft: #d6d6d6;
    --mark-tone: #3b3b3d;
    --mark-line: #444446;
  }
  * { box-sizing: border-box; margin: 0; padding: 0; }
  html, body {
    width: 1200px;
    height: 1200px;
    overflow: hidden;
    background: var(--page-bg);
    font-family: "Montserrat", sans-serif;
  }
  .canvas {
    width: 1200px;
    height: 1200px;
    display: flex;
    flex-direction: column;
    align-items: center;
    justify-content: center;
    gap: 60px;
  }
  .card {
    position: relative;
    width: 840px;
    height: 480px;
    background: var(--card-bg);
    border: 1px solid var(--card-edge);
    border-radius: 36px;
    overflow: hidden;
  }

  /* front */
  .contact-block {
    position: absolute;
    left: 70px;
    top: 190px;
    color: var(--text-light);
  }
  .person-name {
    font-size: 38px;
    font-weight: 600;
    letter-spacing: 1px;
    line-height: 1;
  }
  .person-title {
    font-size: 17px;
    font-weight: 400;
    letter-spacing: 1px;
    margin: 6px 0 0 20px;
    color: var(--text-soft);
  }
  .contact-list {
    list-style: none;
    margin: 22px 0 0 44px;
  }
  .contact-list li {
    display: flex;
    align-items: flex-start;
    gap: 10px;
    font-size: 17px;
    line-height: 1.35;
    color: var(--text-light);
  }
  .contact-list svg {
    width: 18px;
    height: 18px;
    flex: none;
    margin-top: 2px;
    fill: var(--text-light);
  }
  .contact-list .social { margin-top: 14px; padding-left: 28px; }

  .front-mark {
    position: absolute;
    right: 80px;
    top: 90px;
    display: flex;
    align-items: center;
    gap: 16px;
  }
  .plain-circle {
    border: 4px solid var(--mark-line);
    border-radius: 50%;
  }
  .front-mark .plain-circle { width: 56px; height: 56px; }
  .brand-name {
    font-weight: 600;
    color: var(--mark-tone);
    letter-spacing: 4px;
    text-transform: uppercase;
  }
  .front-mark .brand-name { font-size: 34px; }

  /* back */
  .back-lockup {
    position: absolute;
    inset: 0;
    display: flex;
    align-items: center;
    justify-content: center;
    gap: 34px;
  }
  .back-lockup .plain-circle { width: 150px; height: 150px; }
  .divider {
    width: 2px;
    height: 160px;
    background: var(--mark-line);
  }
  .back-lockup .brand-name { font-size: 52px; letter-spacing: 6px; }
</style>
</head>
<body>
<main class="canvas">

  <section class="card card-front">
    <div class="front-mark">
      <span class="plain-circle"></span>
      <span class="brand-name">Marble Crest</span>
    </div>

    <div class="contact-block">
      <h1 class="person-name">FULL NAME</h1>
      <p class="person-title">TITLE</p>
      <ul class="contact-list">
        <li>
          <svg viewBox="0 0 24 24" aria-hidden="true"><path d="M6.6 10.8a15.1 15.1 0 0 0 6.6 6.6l2.2-2.2c.3-.3.7-.4 1-.2 1.1.4 2.3.6 3.6.6.6 0 1 .4 1 1V20c0 .6-.4 1-1 1A17 17 0 0 1 3 4c0-.6.4-1 1-1h3.5c.6 0 1 .4 1 1 0 1.3.2 2.5.6 3.6.1.3 0 .7-.2 1z"/></svg>
          <span>(000) 000 0000</span>
        </li>
        <li>
          <svg viewBox="0 0 24 24" aria-hidden="true"><path d="M7 2h9l3 3v5h1a2 2 0 0 1 2 2v8a2 2 0 0 1-2 2H4a2 2 0 0 1-2-2v-8a2 2 0 0 1 2-2h3zm2 2v6h8V6h-3V4zm-3 9v2h3v-2zm5 0v2h3v-2zm5 0v2h3v-2zm-10 4v2h3v-2zm5 0v2h3v-2zm5 0v2h3v-2z"/></svg>
          <span>(000) 000 0000</span>
        </li>
        <li>
          <svg viewBox="0 0 24 24" aria-hidden="true"><path d="M2 5h20v14H2zm2 2v.5l8 5.5 8-5.5V7zm0 3v7h16v-7l-8 5.5z"/></svg>
          <span>email@company.com</span>
        </li>
        <li>
          <svg viewBox="0 0 24 24" aria-hidden="true"><path d="M12 2a7 7 0 0 0-7 7c0 5.2 7 13 7 13s7-7.8 7-13a7 7 0 0 0-7-7zm0 9.5A2.5 2.5 0 1 1 12 6.5a2.5 2.5 0 0 1 0 5z"/></svg>
          <span>123 Name Street, 000<br>Your City, 00000-000</span>
        </li>
        <li class="social"><span>@MarbleCrest</span></li>
      </ul>
    </div>
  </section>

  <section class="card card-back">
    <div class="back-lockup">
      <span class="plain-circle"></span>
      <span class="divider"></span>
      <span class="brand-name">Marble Crest</span>
    </div>
  </section>

</main>
</body>
</html>
```